Business Card Design

I need a good card to sell my talents in the music field and get my name known as a musician/Guitarist

Industry/Entity Type

Business

Contact Information for Business Card

Leonard Vasquez Musician/Guitarist

```html
<!DOCTYPE html>
<html lang="en">
<head>
<meta charset="utf-8">
<title>Leonard Vasquez – Business Card</title>
<link rel="stylesheet" href="https://fonts.googleapis.com/css2?family=Marcellus&display=swap">
<style>
  :root {
    --backdrop: #e9e4de;
    --card-red-light: #f21a1a;
    --card-red: #d40a0a;
    --card-red-dark: #a80000;
    --card-black-light: #5a5a5a;
    --card-black: #2e2e2e;
    --card-black-dark: #1a1a1a;
    --ink-white: #ffffff;
    --ink-soft: rgba(255, 255, 255, 0.9);
  }
  * { box-sizing: border-box; margin: 0; padding: 0; }
  html, body {
    width: 1200px;
    height: 705px;
    overflow: hidden;
    background: var(--backdrop);
    font-family: "Marcellus", "Georgia", serif;
  }
  .stage {
    position: relative;
    width: 1200px;
    height: 705px;
    display: flex;
    justify-content: center;
    align-items: center;
    gap: 70px;
  }
  .card {
    position: relative;
    width: 330px;
    height: 490px;
    border-radius: 22px;
    color: var(--ink-white);
    box-shadow: 0 14px 30px rgba(0, 0, 0, 0.28);
    overflow: hidden;
  }
  .card--front {
    background: linear-gradient(135deg, var(--card-red-dark) 0%, var(--card-red) 35%, var(--card-red-light) 55%, var(--card-red) 75%, var(--card-red-dark) 100%);
  }
  .card--back {
    background: radial-gradient(circle at 50% 40%, var(--card-black-light) 0%, var(--card-black) 55%, var(--card-black-dark) 100%);
  }
  .music-motif {
    position: absolute;
    border-radius: 8px;
    background: linear-gradient(100deg, rgba(255,255,255,0.85), rgba(255,255,255,0.6));
  }
  .card--front .music-motif { left: 95px; top: 55px; width: 140px; height: 85px; }
  .card--back .music-motif { left: 60px; top: 140px; width: 205px; height: 130px; }

  .rule {
    position: absolute;
    left: 45px;
    right: 45px;
    height: 2px;
    background: var(--ink-white);
  }
  .rule--top { top: 170px; }
  .rule--middle { top: 238px; }
  .rule--bottom { top: 296px; }

  .name {
    position: absolute;
    top: 185px;
    width: 100%;
    text-align: center;
    font-size: 22px;
    letter-spacing: 0.3px;
  }
  .role {
    position: absolute;
    width: 100%;
    text-align: center;
    font-size: 13px;
    color: var(--ink-soft);
  }
  .card--front .role { top: 214px; }
  .card--back .role { top: 300px; font-size: 20px; }

  .address {
    position: absolute;
    top: 316px;
    width: 100%;
    text-align: center;
    font-size: 14px;
    line-height: 1.45;
  }
  .contact {
    position: absolute;
    top: 378px;
    width: 100%;
    list-style: none;
    text-align: center;
    font-size: 14px;
    line-height: 1.9;
  }
  .contact li { display: flex; justify-content: center; align-items: center; gap: 7px; }
  .contact svg { width: 12px; height: 12px; fill: var(--ink-white); }
</style>
</head>
<body>
  <main class="stage">
    <article class="card card--front">
      <div class="music-motif" role="img" aria-label="White treble clef and music notes on a slanted staff"></div>
      <div class="rule rule--top"></div>
      <h1 class="name">Leonard Vasquez</h1>
      <p class="role">Musician | Guitaris</p>
      <div class="rule rule--middle"></div>
      <p class="address">42 Birchwood Road, Hollow Creek<br>New York 10577</p>
      <ul class="contact">
        <li>
          <svg viewBox="0 0 24 24" aria-hidden="true"><path d="M6.6 10.8a15.1 15.1 0 0 0 6.6 6.6l2.2-2.2a1 1 0 0 1 1-.25 11.4 11.4 0 0 0 3.6.57 1 1 0 0 1 1 1V20a1 1 0 0 1-1 1A17 17 0 0 1 3 4a1 1 0 0 1 1-1h3.5a1 1 0 0 1 1 1c0 1.25.2 2.45.57 3.57a1 1 0 0 1-.25 1z"/></svg>
          914-555-0182
        </li>
        <li>
          <svg viewBox="0 0 24 24" aria-hidden="true"><path d="M12 2a10 10 0 1 0 0 20 10 10 0 0 0 0-20zm6.9 6h-2.9a15.6 15.6 0 0 0-1.4-3.6A8 8 0 0 1 18.9 8zM12 4a14 14 0 0 1 1.9 4h-3.8A14 14 0 0 1 12 4zM4.3 14a8 8 0 0 1 0-4h3.4a16 16 0 0 0 0 4zm.8 2h2.9a15.6 15.6 0 0 0 1.4 3.6A8 8 0 0 1 5.1 16zM8 8H5.1a8 8 0 0 1 4.3-3.6A15.6 15.6 0 0 0 8 8zm4 12a14 14 0 0 1-1.9-4h3.8A14 14 0 0 1 12 20zm2.3-6H9.7a14.7 14.7 0 0 1 0-4h4.6a14.7 14.7 0 0 1 0 4zm.3 5.6a15.6 15.6 0 0 0 1.4-3.6h2.9a8 8 0 0 1-4.3 3.6zM16.3 14a16 16 0 0 0 0-4h3.4a8 8 0 0 1 0 4z"/></svg>
          leonardvasquez.com
        </li>
      </ul>
    </article>

    <article class="card card--back">
      <div class="music-motif" role="img" aria-label="White treble clef and music notes on a slanted staff"></div>
      <p class="role">Musician | Guitaris</p>
    </article>
  </main>
</body>
</html>
```